Author/ Speaker Business Card design

I need a business card designed that will go with the branding that is already on my book and website. I like clean and straightforward, but I am not opposed to something more 'innovative'.

Target Market(s)

Colleges and Universities, educational institutions

Industry/Entity Type

Education

Contact Information for Business Card

Standard size. It should be able to be printed on good quality white or ivory paper.

Font styles to use
Sans Serif

Colors
0355a3

Requirements
Must have
• There's a blue on my website. It should have some blue. My logo is at the top. It should have the logo incorporated somewhere on it. My name, Author | Speaker | Teacher | Trainer, my phone number (+31 64-207 5819), my email address (milo@theboldlearner.example), Social media icons (twitter, Instagram, LinkedIn) with the addresses (twitter @writermilofenwick, Instagram - theboldlearner, LinkedIn - theboldlearner) By they way, the website is www.theboldlearner.example. There is a photo of the book on the website. Also, my full name is Milo Fenwick
Nice to have
• Try to use the font that is on the website and book. Also, if you could get that blue, that would be great.
Should not have
• My photo

```html
<!DOCTYPE html>
<html lang="en">
<head>
<meta charset="utf-8">
<title>Milo Fenwick – Business Card</title>
<link rel="stylesheet" href="https://fonts.googleapis.com/css2?family=Arimo:wght@400;700&display=swap">
<style>
  :root {
    --brand-blue: #0355a3;
    --card-white: #f4f4f2;
    --panel-grey: #cfcfcf;
    --ink: #1d1d1d;
    --icon-dark: #222222;
    --backdrop: #5a88ab;
  }
  * { box-sizing: border-box; margin: 0; padding: 0; }
  html, body {
    width: 1200px; height: 1018px; overflow: hidden;
    background: var(--backdrop);
    font-family: "Arimo", Arial, sans-serif;
  }
  .card {
    position: absolute; left: 320px; top: 76px;
    width: 560px; height: 866px;
    background: var(--card-white);
    box-shadow: 0 18px 40px rgba(0,0,0,0.25);
  }
  .logo-block {
    position: absolute; left: 78px; top: 22px;
    width: 404px; height: 300px;
    background: var(--brand-blue);
    display: flex; align-items: center; justify-content: center;
  }
  .logo-name {
    color: #ffffff; font-weight: 700; font-size: 40px; letter-spacing: 0.01em;
  }
  .identity {
    position: absolute; left: 0; top: 360px; width: 100%;
    text-align: center; color: var(--ink);
  }
  .identity-name {
    font-weight: 700; font-size: 34px; letter-spacing: 0.22em;
  }
  .identity-roles {
    margin-top: 8px; font-size: 17px; letter-spacing: 0.02em;
  }
  .contact-panel {
    position: absolute; left: 0; top: 452px;
    width: 100%; height: 322px;
    background: var(--panel-grey);
  }
  .rule {
    position: absolute; height: 4px; background: var(--brand-blue);
  }
  .rule-top { left: 110px; top: 36px; width: 360px; }
  .rule-bottom { left: 96px; top: 296px; width: 360px; }
  .contact-list {
    position: absolute; left: 96px; top: 62px; list-style: none;
  }
  .contact-item {
    display: flex; align-items: center; gap: 14px;
    height: 37px; font-size: 22px; color: var(--ink);
  }
  .contact-icon {
    width: 24px; height: 24px; flex: none;
  }
</style>
</head>
<body>
  <main class="card">
    <div class="logo-block">
      <span class="logo-name">The Bold Learner</span>
    </div>

    <section class="identity">
      <h1 class="identity-name">MILO FENWICK</h1>
      <p class="identity-roles">AUTHOR | SPEAKER | TEACHER | TRAINER</p>
    </section>

    <section class="contact-panel">
      <div class="rule rule-top"></div>
      <ul class="contact-list">
        <li class="contact-item">
          <svg class="contact-icon" viewBox="0 0 24 24" aria-hidden="true">
            <circle cx="12" cy="12" r="12" fill="var(--icon-dark)"/>
            <path d="M8.3 6.5l2 2.3-1.2 1.6c.8 1.7 2 2.9 3.7 3.7l1.6-1.2 2.3 2-1.2 1.9c-4.2-.4-7.7-3.9-8.1-8.1z" fill="#fff"/>
          </svg>
          <span>+31 64-207 5819</span>
        </li>
        <li class="contact-item">
          <svg class="contact-icon" viewBox="0 0 24 24" aria-hidden="true">
            <circle cx="12" cy="12" r="12" fill="var(--icon-dark)"/>
            <rect x="6" y="8" width="12" height="8.5" fill="none" stroke="#fff" stroke-width="1.4"/>
            <path d="M6 8l6 5 6-5" fill="none" stroke="#fff" stroke-width="1.4"/>
          </svg>
          <span>milo@theboldlearner.example</span>
        </li>
        <li class="contact-item">
          <svg class="contact-icon" viewBox="0 0 24 24" aria-hidden="true">
            <circle cx="12" cy="12" r="12" fill="var(--icon-dark)"/>
          </svg>
          <span>writermilofenwick</span>
        </li>
        <li class="contact-item">
          <svg class="contact-icon" viewBox="0 0 24 24" aria-hidden="true">
            <circle cx="12" cy="12" r="12" fill="var(--icon-dark)"/>
          </svg>
          <span>theboldlearner</span>
        </li>
        <li class="contact-item">
          <svg class="contact-icon" viewBox="0 0 24 24" aria-hidden="true">
            <circle cx="12" cy="12" r="12" fill="var(--icon-dark)"/>
          </svg>
          <span>theboldlearner</span>
        </li>
        <li class="contact-item">
          <svg class="contact-icon" viewBox="0 0 24 24" aria-hidden="true">
            <circle cx="12" cy="12" r="12" fill="var(--icon-dark)"/>
            <g fill="none" stroke="#fff" stroke-width="1.2">
              <circle cx="12" cy="12" r="6.5"/>
              <ellipse cx="12" cy="12" rx="2.8" ry="6.5"/>
              <path d="M5.5 12h13M6.5 8.8h11M6.5 15.2h11"/>
            </g>
          </svg>
          <span>www.theboldlearner.example</span>
        </li>
      </ul>
      <div class="rule rule-bottom"></div>
    </section>
  </main>
</body>
</html>
```